Lifestyle management firm needs PDF/brochure created from existing web content for InDesign

We are a boutique lifestyle management company based in NY with offices in San Francisco. We looking to create a brochure directed towards larger corporate partners and developers. We have already created the web content for this branch of our business. We would like to create a PDF presentation of the web content that we can use for in person presentations and to email to potential partners and clients. It should be a basic brochure version of the web content. The website is on sitebloc.net and we need to take that design and recreate it in in Illustrator or In Design so that it can ultimately be saved as a PDF and emailed or handed out as a presentation.

See www.harborlanestewards.com

Thank you,

Marnie

Target Market(s)

Real estate developers and corporate partners

Industry/Entity Type

Boutique

Requirements
Must have
• Should be based on the existing web content. Should be easy to email. Should be created in InDesign or illustrator.
Nice to have
• An easy to print format so we have the option to present it in person.

```html
<!DOCTYPE html>
<html lang="en">
<head>
<meta charset="utf-8">
<title>Harbor Lane – Unique Programming and Experiences</title>
<link rel="stylesheet" href="https://fonts.googleapis.com/css2?family=Arimo:wght@400&display=swap">
<style>
  :root {
    --paper: #ffffff;
    --ink: #1a1a1a;
    --accent: #1fa3dd;
    --sky-top: #a9c4dc;
    --sky-low: #d9e3ea;
    --city: #8a8374;
    --park: #4f7f3a;
  }
  html, body {
    margin: 0;
    padding: 0;
    overflow: hidden;
    background: var(--paper);
  }
  .page {
    position: relative;
    width: 927px;
    height: 1200px;
    overflow: hidden;
    background: var(--paper);
    font-family: "Arimo", Arial, sans-serif;
    color: var(--ink);
  }
  .block {
    position: absolute;
    left: 66px;
    margin: 0;
    white-space: nowrap;
  }
  .lead-title {
    top: 58px;
    font-size: 19px;
    font-weight: 400;
    color: var(--accent);
  }
  .lead-text {
    top: 108px;
    font-size: 18.4px;
    line-height: 25.5px;
  }
  .section-title {
    font-size: 15.5px;
    font-weight: 400;
    color: var(--accent);
    line-height: 20px;
  }
  .section-text {
    font-size: 15px;
    line-height: 21.8px;
  }
  .hero-view {
    position: absolute;
    left: 66px;
    top: 949px;
    width: 791px;
    height: 196px;
    background: linear-gradient(180deg, var(--sky-top) 0%, var(--sky-low) 30%, var(--city) 45%, var(--park) 70%, var(--city) 100%);
  }
</style>
</head>
<body>
<main class="page">
  <h1 class="block lead-title">Unique Programming and Experiences</h1>
  <p class="block lead-text">In addition to our day-to-day care of residents, Harbor Lane can curate unitque programming<br>- memorable events that educate and enliven residents and that foster community within<br>the building.&nbsp; These would be customized to meet the interests of the residents (some may<br>be at an additional charge) but examples include:</p>

  <h2 class="block section-title" style="top:235px">Unique Programming and Experiences</h2>
  <p class="block section-text" style="top:278px">In addition to our day-to-day care of residents, Harbor Lane can curate unitque programming - memorable<br>events that educate and enliven residents and that foster community within the building.&nbsp; These would be<br>customized to meet the interests of the residents (some may be at an additional charge) but examples<br>include:</p>

  <h2 class="block section-title" style="top:387px">East Meets West</h2>
  <p class="block section-text" style="top:430px">A leading wellness expert will educate residents on how Eastern &amp; Western health philosophies are being<br>integrated together.&nbsp; Topics can include nutrition, juicing, sprouting, meditation, sleep, exercise and offer<br>hands-on experience of yoga, acupuncture, energy work and more.</p>

  <h2 class="block section-title" style="top:518px">Scent Design</h2>
  <p class="block section-text" style="top:561px">Scent is the strongest link to our memory and emotion.&nbsp; You can create an emotional connection with a<br>resident through their nose and take branding to the next level.&nbsp; Scent helps create a new environment.<br>Each season we will co-create (with the building) a custom scent for the building’s public spaces and of-<br>fer the scent as a gift to residents.&nbsp; They can travel with this scent to their other residences and enjoy the<br>emotional and enduring experience in all their atmospheres.</p>

  <h2 class="block section-title" style="top:693px">Gallery Tours and Studio Visits</h2>
  <p class="block section-text" style="top:736px">A leading NYC gallery owner will lead gallery tours to reveal what’s hot and happening in the NYC and<br>worldwide art market.&nbsp; Art forward neighborhoods such as Chlesea, Upper East Side, Lower East Side<br>and Brooklyn will be explored.&nbsp; For collectors, art advisory and introductions to important galleries will be<br>made based on areas of interest.&nbsp; Artist studio visits can also be arranged.</p>

  <h2 class="block section-title" style="top:846px">Tech Mystery to Mastery</h2>
  <p class="block section-text" style="top:888px">Tech geniuses teach tricks of the trade for all Nexa devices (Nexaphone, Nexatab, Nexaplay, Nexabook) such as how to share<br>music in an easier way, increase the speed of a Nexatab or better organize photos.</p>

  <div class="hero-view" role="img" aria-label="Panoramic view through tall windows over a city park surrounded by apartment towers, with a resident looking out"></div>
</main>
</body>
</html>
```